8' x 22' Enclosed work trailer

I just purchased a new work trailer and want a badass design for the exterior. Either a wrap, lettering or combo to match my truck. I have a kitchen & bathroom remodeling company - Renovo Crafters. I think it should include my logo and possibly a larger photo of a sweet kitchen and bathroom just like my old trailer. I'm attaching pics of my old trailer for reference, my existing truck, my new trailer and logo. Excited to see the results!

```html
<!DOCTYPE html>
<html lang="en">
<head>
<meta charset="utf-8">
<title>Renovo Crafters – Trailer Graphics</title>
<link href="https://fonts.googleapis.com/css2?family=Lato:wght@400;700;900&family=Playball&family=Allura&display=swap" rel="stylesheet">
<style>
  :root{
    --sheet:#e0e0e0;
    --white:#ffffff;
    --brand-blue:#0866a8;
    --tag-blue:#1d55a3;
    --ink:#161616;
    --label:#222222;
    --tile-light:#eceef0;
    --tile-mid:#c9cdd1;
    --wood:#9a7551;
    --cabinet:#8f959b;
    --wall-grey:#8d9196;
    --carpet:#b9b5ad;
  }
  *{box-sizing:border-box;margin:0;padding:0}
  html,body{width:1200px;height:1086px;overflow:hidden;background:var(--sheet)}
  body{position:relative;font-family:'Lato',sans-serif}

  .panel{position:absolute;background:var(--white);overflow:hidden}
  .panel svg.art{position:absolute;inset:0;width:100%;height:100%}
  .panel--side{left:118px;top:172px;width:964px;height:350px}
  .panel--back-plain{left:253px;top:615px;width:322px;height:322px}
  .panel--back-photo{left:625px;top:615px;width:322px;height:322px}

  .centered{position:absolute;transform:translateX(-50%);white-space:nowrap;text-align:center}
  .brand-name{font-family:'Lato',sans-serif;font-weight:900;color:var(--brand-blue);line-height:.95;letter-spacing:.5px}
  .tagline{font-family:'Playball',cursive;color:var(--tag-blue)}
  .help-line{font-family:'Allura',cursive;color:var(--white)}
  .phone{font-family:'Lato',sans-serif;font-weight:900;color:var(--white);display:flex;align-items:center;gap:4px;line-height:1}
  .phone svg{flex:none}
  .web-band{position:absolute;background:linear-gradient(90deg,rgba(255,255,255,0),rgba(255,255,255,.95) 15%,rgba(255,255,255,.95) 85%,rgba(255,255,255,0));}
  .web{font-family:'Lato',sans-serif;color:var(--ink);letter-spacing:4px}
  .web b{font-weight:900}

  .sheet-label{position:absolute;transform:translateX(-50%);font-size:22px;letter-spacing:4px;color:var(--label);font-weight:400}
</style>
</head>
<body>

<!-- SIDE -->
<section class="panel panel--side">
  <svg class="art" viewBox="0 0 964 350" preserveAspectRatio="none">
    <defs>
      <linearGradient id="bathFade" x1="0" x2="1">
        <stop offset="0" stop-color="#fff"/>
        <stop offset=".35" stop-color="var(--tile-light)"/>
        <stop offset="1" stop-color="var(--tile-mid)"/>
      </linearGradient>
      <linearGradient id="kitchenTone" x1="0" y1="0" x2="0" y2="1">
        <stop offset="0" stop-color="var(--wood)"/>
        <stop offset=".3" stop-color="#e6e7e8"/>
        <stop offset=".65" stop-color="var(--cabinet)"/>
        <stop offset="1" stop-color="#dcdcdc"/>
      </linearGradient>
      <linearGradient id="roomTone" x1="0" y1="0" x2="0" y2="1">
        <stop offset="0" stop-color="var(--wall-grey)"/>
        <stop offset=".5" stop-color="#a3a6a9"/>
        <stop offset="1" stop-color="var(--carpet)"/>
      </linearGradient>
    </defs>
    <rect x="250" y="0" width="260" height="350" fill="url(#bathFade)" role="img" aria-label="Photo of a remodeled white bathroom with glass walk-in shower"/>
    <rect x="510" y="0" width="263" height="350" fill="url(#kitchenTone)" role="img" aria-label="Photo of a modern kitchen with wood upper cabinets and range hood"/>
    <rect x="778" y="0" width="186" height="350" fill="url(#roomTone)" role="img" aria-label="Photo of a finished basement with bar and carpet"/>
    <polygon points="0,254 184,200 638,350 0,350" fill="var(--brand-blue)"/>
    <polyline points="0,254 184,200 642,352" fill="none" stroke="var(--ink)" stroke-width="5"/>
  </svg>
  <div class="centered brand-name" style="left:186px;top:68px;font-size:48px">Renovo<br>Crafters</div>
  <div class="centered tagline" style="left:187px;top:150px;font-size:22px">“Unsurpassed Quality &amp; Design”</div>
  <div class="centered help-line" style="left:188px;top:238px;font-size:26px">We’re always happy to help</div>
  <div class="centered phone" style="left:190px;top:270px;font-size:44px">
    <svg width="30" height="30" viewBox="0 0 24 24"><path fill="#fff" d="M6.6 10.8a15.1 15.1 0 0 0 6.6 6.6l2.2-2.2c.3-.3.7-.4 1-.2 1.1.4 2.3.6 3.6.6.6 0 1 .4 1 1V20c0 .6-.4 1-1 1A17 17 0 0 1 3 4c0-.6.4-1 1-1h3.5c.6 0 1 .4 1 1 0 1.3.2 2.5.6 3.6.1.3 0 .7-.2 1z"/></svg>
    555-204-7310
  </div>
  <div class="web-band" style="left:25px;top:316px;width:340px;height:20px"></div>
  <div class="centered web" style="left:191px;top:318px;font-size:13px">WWW.<b>RENOVO-CRAFTERS</b>.COM</div>
</section>
<div class="sheet-label" style="left:606px;top:540px">SIDE</div>

<!-- BACK 1 -->
<section class="panel panel--back-plain">
  <svg class="art" viewBox="0 0 322 322">
    <polygon points="0,224 156,179 322,236 322,322 0,322" fill="var(--brand-blue)"/>
    <polyline points="-2,224 156,179 324,236" fill="none" stroke="var(--ink)" stroke-width="5"/>
  </svg>
  <div class="centered brand-name" style="left:152px;top:40px;font-size:46px">Renovo<br>Crafters</div>
  <div class="centered tagline" style="left:161px;top:129px;font-size:19px">“Unsurpassed Quality &amp; Design”</div>
  <div class="centered help-line" style="left:159px;top:217px;font-size:23px">We’re always happy to help</div>
  <div class="centered phone" style="left:162px;top:244px;font-size:38px">
    <svg width="26" height="26" viewBox="0 0 24 24"><path fill="#fff" d="M6.6 10.8a15.1 15.1 0 0 0 6.6 6.6l2.2-2.2c.3-.3.7-.4 1-.2 1.1.4 2.3.6 3.6.6.6 0 1 .4 1 1V20c0 .6-.4 1-1 1A17 17 0 0 1 3 4c0-.6.4-1 1-1h3.5c.6 0 1 .4 1 1 0 1.3.2 2.5.6 3.6.1.3 0 .7-.2 1z"/></svg>
    555-204-7310
  </div>
  <div class="web-band" style="left:10px;top:284px;width:302px;height:18px"></div>
  <div class="centered web" style="left:161px;top:286px;font-size:11.5px;letter-spacing:3.5px">WWW.<b>RENOVO-CRAFTERS</b>.COM</div>
</section>
<div class="sheet-label" style="left:422px;top:958px">BACK 1</div>

<!-- BACK 2 -->
<section class="panel panel--back-photo">
  <svg class="art" viewBox="0 0 322 322">
    <defs>
      <linearGradient id="topFade" x1="0" y1="0" x2="0" y2="1">
        <stop offset="0" stop-color="#fff"/>
        <stop offset="1" stop-color="#fff" stop-opacity="0"/>
      </linearGradient>
    </defs>
    <rect x="0" y="115" width="100" height="135" fill="var(--tile-mid)" role="img" aria-label="Photo of a remodeled bathroom with glass shower"/>
    <rect x="104" y="115" width="115" height="135" fill="var(--cabinet)" role="img" aria-label="Photo of a modern kitchen"/>
    <rect x="223" y="115" width="99" height="135" fill="var(--carpet)" role="img" aria-label="Photo of a finished basement with bar"/>
    <rect x="0" y="110" width="322" height="50" fill="url(#topFade)"/>
    <polygon points="0,244 158,201 322,250 322,322 0,322" fill="var(--brand-blue)"/>
    <polyline points="-2,244 158,201 324,250" fill="none" stroke="var(--ink)" stroke-width="5"/>
  </svg>
  <div class="centered brand-name" style="left:157px;top:36px;font-size:46px">Renovo<br>Crafters</div>
  <div class="centered tagline" style="left:161px;top:122px;font-size:19px">“Unsurpassed Quality &amp; Design”</div>
  <div class="centered help-line" style="left:157px;top:225px;font-size:22px">We’re always happy to help</div>
  <div class="centered phone" style="left:161px;top:250px;font-size:36px">
    <svg width="25" height="25" viewBox="0 0 24 24"><path fill="#fff" d="M6.6 10.8a15.1 15.1 0 0 0 6.6 6.6l2.2-2.2c.3-.3.7-.4 1-.2 1.1.4 2.3.6 3.6.6.6 0 1 .4 1 1V20c0 .6-.4 1-1 1A17 17 0 0 1 3 4c0-.6.4-1 1-1h3.5c.6 0 1 .4 1 1 0 1.3.2 2.5.6 3.6.1.3 0 .7-.2 1z"/></svg>
    555-204-7310
  </div>
  <div class="web-band" style="left:10px;top:289px;width:302px;height:17px"></div>
  <div class="centered web" style="left:161px;top:290px;font-size:11.5px;letter-spacing:3.5px">WWW.<b>RENOVO-CRAFTERS</b>.COM</div>
</section>
<div class="sheet-label" style="left:786px;top:958px">BACK 2</div>

</body>
</html>
```